Criação de Papelaria Profissional para Construção & Engenharia
" Empresa que atua em incorporação imobiliária, administrando a construção de edifícios "

```html
<!DOCTYPE html>
<html lang="pt-BR">
<head>
<meta charset="UTF-8">
<title>Timbrado — Torres Vale Engenharia</title>
<link rel="stylesheet" href="https://fonts.googleapis.com/css2?family=Montserrat:wght@500;600;700;800&display=swap">
<style>
  :root {
    --brand-blue: #22468c;
    --brand-gray: #3b4048;
    --backdrop: #e4e5e7;
    --paper: #ffffff;
    --footer-text: #ffffff;
  }
  * { margin: 0; padding: 0; box-sizing: border-box; }
  html, body { width: 1200px; height: 1200px; overflow: hidden; }
  body {
    background: var(--backdrop);
    font-family: "Montserrat", Arial, sans-serif;
    position: relative;
  }
  .presentation-frame { position: absolute; inset: 0; }
  .section-title {
    position: absolute; top: 26px; left: 0; width: 1200px;
    text-align: center; font-weight: 800; font-size: 30px;
    letter-spacing: 1px; color: var(--brand-gray);
  }
  .letterhead {
    position: absolute; left: 332px; top: 118px;
    width: 536px; height: 758px;
    background: var(--paper);
    box-shadow: 0 10px 30px rgba(0,0,0,.18);
  }
  .letterhead-brand {
    position: absolute; left: 44px; top: 44px;
    display: flex; align-items: center; gap: 12px;
  }
  .brand-square { width: 34px; height: 34px; background: var(--brand-blue); }
  .brand-name { font-weight: 700; font-size: 17px; color: var(--brand-gray); line-height: 1; letter-spacing: .5px; }
  .brand-sub { display: block; font-weight: 600; font-size: 8px; letter-spacing: 5px; color: var(--brand-gray); margin-top: 5px; }
  .letterhead-footer {
    position: absolute; left: 0; bottom: 34px; width: 100%; height: 30px;
    background: var(--brand-blue);
    display: flex; align-items: center; justify-content: space-between;
    padding: 0 22px; color: var(--footer-text); font-size: 8px; font-weight: 500;
  }
  .contact { display: flex; align-items: center; gap: 5px; }
  .contact svg { width: 10px; height: 10px; }
  .social-dot { width: 9px; height: 9px; border-radius: 50%; background: var(--footer-text); }
  .signature-brand {
    position: absolute; left: 0; top: 1080px; width: 1200px;
    display: flex; justify-content: center; align-items: center; gap: 18px;
  }
  .signature-brand .brand-square { width: 66px; height: 66px; }
  .signature-brand .brand-name { font-size: 34px; }
  .signature-brand .brand-sub { font-size: 14px; letter-spacing: 11px; margin-top: 8px; }
</style>
</head>
<body>
  <svg class="presentation-frame" width="1200" height="1200" viewBox="0 0 1200 1200">
    <g fill="none" stroke="var(--brand-blue)" stroke-width="7">
      <path d="M450 44 H96 Q50 44 50 90 V1030 Q50 1076 96 1076 H400"/>
      <path d="M750 44 H1104 Q1150 44 1150 90 V1030 Q1150 1076 1104 1076 H800"/>
    </g>
  </svg>
  <div class="section-title">TIMBRADO</div>

  <section class="letterhead">
    <div class="letterhead-brand">
      <span class="brand-square"></span>
      <span class="brand-name">TORRES VALE<span class="brand-sub">ENGENHARIA</span></span>
    </div>
    <footer class="letterhead-footer">
      <span class="contact">
        <svg viewBox="0 0 10 10"><path d="M2 1 L4 3 L3 4 Q4 6 6 7 L7 6 L9 8 L8 9 Q3 9 1 2 Z" fill="#fff"/></svg>
        (11) 4000-1234
      </span>
      <span class="contact">
        <svg viewBox="0 0 10 10"><rect x="1" y="2" width="8" height="6" fill="none" stroke="#fff"/><path d="M1 2 L5 5 L9 2" fill="none" stroke="#fff"/></svg>
        contato@torresvale.com.br
      </span>
      <span class="contact"><span class="social-dot"></span>/torresvaleeng</span>
      <span class="contact"><span class="social-dot"></span>/torresvale</span>
    </footer>
  </section>

  <div class="signature-brand">
    <span class="brand-square"></span>
    <span class="brand-name">TORRES VALE<span class="brand-sub">ENGENHARIA</span></span>
  </div>
</body>
</html>
```